Velvet Paw Hospital Business Card Design

I need a business card designed for my cat only veterinary clinic. I will upload the logo that I would like included on the card. Please include:
Business Name: The Velvet Paw Hospital
Address: 20947 E. 38th St, Scottsdale, AZ 85371
Phone #: 480-555-6143
Website URL: www.velvetpawvets.com
And the Doctors Name: Marisol Brenn, DVM

```html
<!DOCTYPE html>
<html lang="en">
<head>
<meta charset="utf-8">
<title>The Velvet Paw Hospital – Business Card</title>
<link href="https://fonts.googleapis.com/css2?family=Lato:wght@400;700&display=swap" rel="stylesheet">
<style>
  :root {
    --stage: #4a4a4a;
    --card: #15110e;
    --green: #479743;
    --green-bright: #4fa14a;
    --white: #ffffff;
    --art-top: #120d1c;
    --art-bottom: #3a2670;
  }
  * { box-sizing: border-box; margin: 0; padding: 0; }
  html, body {
    width: 1200px; height: 801px; overflow: hidden;
    background: var(--stage);
    font-family: "Lato", sans-serif;
  }
  .card {
    position: absolute;
    width: 620px; height: 354px;
    background: var(--card);
    border-bottom: 2px solid var(--green-bright);
    border-left: 2px solid var(--green-bright);
    overflow: hidden;
  }
  .card--front { left: 40px; top: 40px; }
  .card--back  { left: 540px; top: 410px; }

  .artwork {
    position: absolute;
    background: linear-gradient(180deg, var(--art-top) 0%, var(--art-bottom) 100%);
  }
  .card--front .artwork { left: 44px; top: 40px; width: 236px; height: 232px; }
  .card--back  .artwork { left: 185px; top: 62px; width: 300px; height: 250px; }

  .divider {
    position: absolute;
    left: 298px; top: 40px;
    width: 1.5px; height: 228px;
    background: var(--green);
  }
  .details {
    position: absolute;
    left: 326px; top: 44px;
    color: var(--white);
  }
  .doctor-name {
    color: var(--green-bright);
    font-weight: 700;
    font-size: 26px;
    letter-spacing: .2px;
    margin-bottom: 26px;
  }
  .address {
    font-size: 15px;
    line-height: 1.45;
    margin-bottom: 18px;
  }
  .contact-line {
    display: flex; align-items: center; gap: 7px;
    font-size: 15px;
    line-height: 1.6;
  }
  .contact-line svg { width: 13px; height: 13px; flex: none; }

  .name-band {
    position: absolute;
    left: 0; right: 0; top: 290px;
    height: 36px;
    background: var(--green);
    color: var(--white);
    font-weight: 700;
    font-size: 25px;
    line-height: 36px;
    padding-left: 184px;
    white-space: nowrap;
  }
</style>
</head>
<body>

<section class="card card--front" aria-label="Business card front">
  <div class="artwork" role="img" aria-label="Colourful folk-art illustration of a cat on a cactus in a starry desert night"></div>
  <div class="divider"></div>
  <div class="details">
    <h1 class="doctor-name">Marisol Brenn, DVM</h1>
    <p class="address">20947 E. 38th St,<br>Scottsdale, AZ 85371</p>
    <p class="contact-line">
      <svg viewBox="0 0 16 16" aria-hidden="true"><path fill="#4fa14a" d="M2 5c0-2 1.5-3 6-3s6 1 6 3v1h-3.5V4.8H5.5V6H2zM4 7h8l2 6.5H2zm4 1.6a2 2 0 1 0 0 4 2 2 0 0 0 0-4z"/></svg>
      480-555-6143
    </p>
    <p class="contact-line">
      <svg viewBox="0 0 16 16" aria-hidden="true"><circle cx="8" cy="8" r="7" fill="#4fa14a"/><path fill="#15110e" d="M4 5.5c1-.5 2 0 2.5 1s-.5 2-1.5 2.2S4 10 4.5 11C3 10 2.7 7 4 5.5zm5.5-2c1.5.3 2.8 1.5 3.2 3-1 .2-1.7-.5-2.2-1.2s-1-1.3-1-1.8zM9 9.5c1 0 2 .6 2 1.6S10 13 9 12.6 8 9.5 9 9.5z"/></svg>
      www.velvetpawvets.com
    </p>
  </div>
  <div class="name-band">The Velvet Paw Hospital</div>
</section>

<section class="card card--back" aria-label="Business card back">
  <div class="artwork" role="img" aria-label="Colourful folk-art illustration of a cat on a cactus in a starry desert night"></div>
</section>

</body>
</html>
```